Real Estate Managemene Company Needs Business Card Design

We have a logo design and just need business cards made now for our business. Please use PDF logo # 3.

Card with Information to be attached shortly.

The card is used for a real estate management company. We will need to add four other employees and their cards.

Industry/Entity Type

Real Estate

Contact Information for Business Card

Tariq Hamdan
President
3187 Thornwick Avenue
Suite C
Fernhollow, OR 97152
Phone 541.417.2286
Fax 541.417.2287
Cell 541.473.8062
vantorp@mailbreeze.net

Once design is approved we will have four other employees
Omar Hamdan
Operations Manager

Nadia Hamdan
Administrative Manager

Faz Hamdan
Principal

We would need to take out the cell # 541.473.8062 out for the remaining three cards.

Requirements
Must have
• Please use logo attached

```html
<!DOCTYPE html>
<html lang="en">
<head>
<meta charset="utf-8">
<title>Brightleaf Management – Business Card</title>
<link rel="stylesheet" href="https://fonts.googleapis.com/css2?family=Montserrat:wght@400;500;800&display=swap">
<style>
  :root {
    --page-bg: #e8e4de;
    --card-red: #d91f33;
    --card-red-dark: #b8162a;
    --card-black: #111112;
    --ink-white: #ffffff;
    --ink-black: #0c0c0c;
  }
  html, body {
    margin: 0;
    padding: 0;
    width: 1200px;
    height: 1022px;
    overflow: hidden;
    background: var(--page-bg);
  }
  .stage {
    width: 1200px;
    height: 1022px;
    display: flex;
    align-items: center;
    justify-content: center;
  }
  .business-card {
    width: 860px;
    height: 492px;
    border-radius: 22px;
    overflow: hidden;
    box-shadow: 0 18px 40px rgba(0,0,0,0.25);
    display: block;
  }
  .card-text { font-family: "Montserrat", Arial, sans-serif; }
  .holder-name { font-weight: 800; font-size: 36px; fill: var(--ink-black); letter-spacing: 0.5px; }
  .holder-title { font-weight: 400; font-size: 17px; fill: var(--ink-white); letter-spacing: 1.5px; }
  .contact-line { font-weight: 400; font-size: 18px; fill: var(--ink-white); letter-spacing: 0.3px; }
  .company-name { font-weight: 800; font-size: 26px; fill: var(--ink-white); letter-spacing: 0.5px; }
  .address-line { font-weight: 400; font-size: 16px; fill: var(--ink-white); letter-spacing: 0.3px; }
  .contact-icon { fill: none; stroke: var(--ink-black); stroke-width: 1.6; }
</style>
</head>
<body>
<main class="stage">
  <svg class="business-card" viewBox="0 0 860 492" xmlns="http://www.w3.org/2000/svg" aria-label="Business card for Tariq Hamdan, President, Brightleaf Management">
    <defs>
      <linearGradient id="red-face" x1="0" y1="0" x2="1" y2="1">
        <stop offset="0" stop-color="var(--card-red)"/>
        <stop offset="1" stop-color="var(--card-red-dark)"/>
      </linearGradient>
    </defs>

    <rect class="card-face" width="860" height="492" fill="url(#red-face)"/>

    <polyline class="accent-stripe" points="262,500 528,292 670,-8" fill="none" stroke="var(--card-black)" stroke-width="13"/>

    <polygon class="black-panel" points="300,492 560,290 700,0 860,0 860,492" fill="var(--card-black)"/>

    <g class="card-text holder">
      <text class="holder-name" x="60" y="312">TARIQ HAMDAN</text>
      <text class="holder-title" x="150" y="338">PRESIDENT</text>
    </g>

    <g class="contact-block">
      <g class="contact-icons" transform="translate(300,0)">
        <path class="contact-icon" d="M2 36c2 5 5 8 10 10l2-3-3-2-2 1c-2-1-3-2-4-4l1-2-2-3z"/>
        <rect class="contact-icon" x="1" y="64" width="12" height="10" rx="1"/>
        <rect class="contact-icon" x="3" y="60" width="8" height="5"/>
        <rect class="contact-icon" x="3" y="89" width="8" height="14" rx="1.5"/>
        <rect class="contact-icon" x="1" y="120" width="12" height="9" rx="1"/>
        <polyline class="contact-icon" points="1,120 7,125 13,120"/>
      </g>
      <g class="card-text">
        <text class="contact-line" x="324" y="48">541.417.2286</text>
        <text class="contact-line" x="324" y="76">541.417.2287</text>
        <text class="contact-line" x="324" y="104">541.473.8062</text>
        <text class="contact-line" x="324" y="132">vantorp@mailbreeze.net</text>
      </g>
    </g>

    <g class="company-mark">
      <rect class="mark-square" x="230" y="172" width="36" height="36" fill="var(--ink-white)"/>
      <g class="card-text">
        <text class="company-name" x="280" y="198">BRIGHTLEAF</text>
        <text class="company-name" x="280" y="230">MANAGEMENT</text>
      </g>
    </g>

    <text class="card-text address-line" x="830" y="462" text-anchor="end">3187 Thornwick Avenue, Suite C, Fernhollow, OR 97152</text>
  </svg>
</main>
</body>
</html>
```